Training Company Needs a Web Design

We are a Training company that needs a website design completed for us. "The Harbor Loft" The website will be a 'community space' specialising in 'Change and Transformation'. It will be a 'space' where individuals can come to find out 'latest news', upcoming events and courses, chat with others and find 'tools and templates'. They will need to login as a 'Member'.

The final design needs to be professional but have a 'fun and interactive' feel and appeal to our target audience who are predominantly corporate individuals.

Target Market(s)

Corporate Individuals - they may have a Change or Project background

Industry/Entity Type

Business Consultant

Number of Pages Required

3 page

Font styles to use
Sans Serif

Requirements
Must have
• Design for 'Home Page'
• A professional and corporate 'feel' but be fun and interactive.
Nice to have
• A 'sense' of how some of the other pages may be designed or laid out.

```html
<!DOCTYPE html>
<html lang="en">
<head>
<meta charset="utf-8">
<title>The Harbor Loft — Home</title>
<link rel="stylesheet" href="https://fonts.googleapis.com/css2?family=Arimo:wght@400;700&display=swap">
<style>
  :root {
    --ink-white: #ffffff;
    --accent-orange: #d8750f;
    --muted-headline: rgba(150, 140, 140, 0.55);
    --shade-top: #151210;
    --shade-mid: #2a1614;
    --shade-low: #3d0d0d;
    --shade-bottom: #4a1011;
  }
  * { margin: 0; padding: 0; box-sizing: border-box; }
  html, body {
    width: 1200px;
    height: 736px;
    overflow: hidden;
    background: var(--shade-top);
    font-family: "Arimo", Arial, sans-serif;
  }
  .page {
    position: relative;
    width: 1200px;
    height: 736px;
    overflow: hidden;
  }
  .hero-backdrop {
    position: absolute;
    inset: 0;
    background:
      radial-gradient(ellipse 70% 40% at 70% 10%, rgba(120, 95, 60, 0.25), transparent 70%),
      radial-gradient(ellipse 60% 45% at 75% 85%, rgba(110, 25, 25, 0.55), transparent 75%),
      radial-gradient(ellipse 40% 35% at 10% 80%, rgba(100, 30, 30, 0.45), transparent 75%),
      linear-gradient(180deg, var(--shade-top) 0%, var(--shade-mid) 35%, var(--shade-low) 65%, var(--shade-bottom) 100%);
  }
  .top-nav a {
    position: absolute;
    top: 39px;
    color: var(--ink-white);
    text-decoration: none;
    font-weight: 700;
    font-size: 13px;
    letter-spacing: 0.3px;
  }
  .top-nav .login { left: 73px; font-size: 15px; top: 37px; }
  .top-nav .news { left: 261px; }
  .top-nav .events { left: 345px; }
  .top-nav .courses { left: 443px; }
  .top-nav .tools { left: 613px; }
  .top-nav .talk { left: 838px; }

  .brand {
    position: absolute;
    left: 74px;
    top: 160px;
    display: flex;
    align-items: center;
    gap: 8px;
    color: var(--accent-orange);
    font-weight: 700;
    font-size: 15px;
    line-height: 18px;
    white-space: nowrap;
  }
  .brand-square {
    width: 14px;
    height: 14px;
    background: var(--accent-orange);
  }
  .expand-icon {
    position: absolute;
    left: 255px;
    top: 148px;
  }
  .news-feed {
    position: absolute;
    left: 262px;
    top: 0;
    width: 260px;
    list-style: none;
  }
  .news-feed li {
    position: absolute;
    left: 0;
    width: 260px;
    white-space: nowrap;
    color: var(--muted-headline);
    font-weight: 700;
    font-size: 24px;
    line-height: 30.5px;
  }
  .join-link {
    position: absolute;
    left: 613px;
    top: 160px;
    color: var(--accent-orange);
    font-weight: 700;
    font-size: 17px;
    text-decoration: none;
  }
  .tagline {
    position: absolute;
    left: 613px;
    top: 218px;
    color: var(--ink-white);
    font-weight: 700;
    font-size: 39px;
    line-height: 44px;
    letter-spacing: 0.2px;
    white-space: nowrap;
  }
</style>
</head>
<body>
<div class="page">
  <div class="hero-backdrop" role="img" aria-label="Photo of an auditorium with rows of red chairs and an audience in the background, darkened"></div>

  <nav class="top-nav">
    <a class="login" href="#">log in</a>
    <a class="news" href="#">NEWS</a>
    <a class="events" href="#">EVENTS</a>
    <a class="courses" href="#">COURSES</a>
    <a class="tools" href="#">TOOLS &amp; TEMPLATES</a>
    <a class="talk" href="#">TALK</a>
  </nav>

  <div class="brand"><span class="brand-square" aria-hidden="true"></span>The Harbor Loft</div>

  <svg class="expand-icon" width="38" height="39" viewBox="0 0 38 39" aria-hidden="true">
    <line x1="19" y1="0" x2="19" y2="39" stroke="#d8750f" stroke-width="2"/>
    <line x1="0" y1="19.5" x2="38" y2="19.5" stroke="#d8750f" stroke-width="2"/>
  </svg>

  <ul class="news-feed">
    <li style="top:226px">The winner takes<br>it all?</li>
    <li style="top:347px">Vela alumni hub<br>meeting<br>with a difference<br>in Brno</li>
    <li style="top:532px">Sofia MBA<br>Event</li>
    <li style="top:659px">CareerWorks Fair<br>Wien<br>March 3–6</li>
  </ul>

  <a class="join-link" href="#">Join Us</a>
  <h1 class="tagline">place of learning,<br>connecting,<br>collaborating and sharing</h1>
</div>
</body>
</html>
```